Flyer for The Quiet Meadow Renewal Ring

I am launching my new offering in my business at an event next Sunday where I have a booth and need a flyer advertising the offering, so the flyer needs to stand out for other practitioners that will also be there on the day offering there services.
This flyer is also what I will use for marketing on social media as well as on the day of the event. See the link below to the offering
http://carolinebirchwood.com.au/quiet-meadow-renewal-ring/

Target Market(s)

Women with body image issues - age range 25 - 65
Women with issues around food such as binge eating, emotional eating, eating disorders.

Industry/Entity Type

Health And Wellness

Font styles to use
Serif
Sans Serif
Script

Colors
f9d9e8
85cae6
cee9f5
fee18a
ffffff
eea4c8

Requirements
Must have
• Colours matching my overall website at carolinebirchwood.com.au - pinks, light blue, gold, white
• Imagery similiar to my Instagram, see below https://www.instagram.com/lanternfieldcarexq/
• - soft, warm, welcoming, nurturing, safe, inviting - see image on sales page for inspiration
• contact details
Should not have
• harsh dark colours or harsh lines

```html
<!DOCTYPE html>
<html lang="en">
<head>
<meta charset="utf-8">
<title>The Quiet Meadow Renewal Ring – Flyer</title>
<link href="https://fonts.googleapis.com/css2?family=Source+Sans+3:ital,wght@0,300;0,400;0,600;1,300&family=PT+Sans+Narrow:wght@700&display=swap" rel="stylesheet">
<style>
  :root{
    --pink:#eea4c8;
    --pink-deep:#e886b6;
    --pink-soft:#f9d9e8;
    --blush-text:#fbe3ef;
    --sky:#85cae6;
    --sky-deep:#2ab8d3;
    --sky-pale:#cee9f5;
    --gold:#fee18a;
    --white:#ffffff;
    --ink:#6d6d72;
  }
  *{margin:0;padding:0;box-sizing:border-box}
  html,body{width:939px;height:1200px;overflow:hidden;background:#f2f2f2}
  .flyer{
    position:relative;width:939px;height:1200px;overflow:hidden;
    background:radial-gradient(ellipse at 60% 80%,#eef0f4 0%,#f7f7f9 45%,#ffffff 80%);
    font-family:"Source Sans 3",sans-serif;font-weight:300;color:var(--ink);
  }
  .decor{position:absolute;inset:0}
  .brand{position:absolute;left:52px;top:56px;display:flex;align-items:center;gap:10px;
    font-family:"Source Sans 3",sans-serif;font-weight:400;font-size:30px;color:var(--sky-deep);letter-spacing:.5px}
  .brand-dot{width:18px;height:18px;border-radius:50%;background:var(--pink-deep)}
  .intro{position:absolute;left:32px;top:0;width:520px;color:var(--white);font-size:18px;line-height:20.5px}
  .intro .title{position:absolute;top:207px;font-size:28px;font-weight:400;white-space:nowrap}
  .intro p{position:absolute;white-space:nowrap}
  .intro .soft{color:var(--blush-text);font-weight:300}
  .intro .soft b{font-weight:400;color:#fff3b8}
  .intro .whisper{color:var(--blush-text);font-weight:400}
  .pitch{position:absolute;right:24px;width:620px;text-align:right}
  .pitch p{white-space:nowrap}
  .call{top:538px;color:var(--sky-deep);font-size:19.5px;line-height:22px;font-weight:400}
  .prison{top:607px;color:var(--pink-deep);font-size:20px;line-height:23px;font-weight:400}
  .ask{top:661px;font-size:17.5px;line-height:20px}
  .ask em{font-style:italic}
  .invite{top:753px;font-size:17.5px;line-height:20px}
  .receive{top:846px;color:var(--pink-deep);font-size:19px;font-weight:400}
  .benefits{position:absolute;right:24px;top:870px;width:660px;list-style:none;text-align:right;font-size:17.5px;line-height:22.5px}
  .benefits li::before{content:"•";color:var(--pink);margin-right:8px}
  .details{position:absolute;left:0;right:0;top:1040px;text-align:center;color:var(--sky-deep)}
  .details .start{font-family:"PT Sans Narrow",sans-serif;font-weight:700;font-size:20px}
  .details .price{font-size:15.5px;line-height:18px;font-weight:400;margin-top:6px}
  .details .early{font-size:13px;font-weight:400}
  .footer{position:absolute;left:0;bottom:0;width:939px;height:73px;
    background:linear-gradient(90deg,var(--sky-deep) 0%,#3fc0da 45%,#c8a6cf 80%,var(--pink-deep) 100%);
    color:var(--white);font-family:"Source Sans 3",sans-serif;font-weight:400}
  .footer .ready{text-align:center;font-size:19px;padding-top:7px}
  .contacts{display:flex;justify-content:space-between;padding:4px 24px 0 34px;font-size:19px}
  .contacts span{display:flex;align-items:center;gap:7px}
  .contacts svg{width:18px;height:18px}
</style>
</head>
<body>
<main class="flyer">
  <svg class="decor" width="939" height="1200" viewBox="0 0 939 1200">
    <defs>
      <radialGradient id="heroTone" cx="50%" cy="45%" r="60%">
        <stop offset="0" stop-color="#f6e4e0"/>
        <stop offset=".55" stop-color="#e9e3ee"/>
        <stop offset="1" stop-color="#bcc6df"/>
      </radialGradient>
      <linearGradient id="fieldTone" x1="0" y1="0" x2="0" y2="1">
        <stop offset="0" stop-color="#e9eef3"/>
        <stop offset=".5" stop-color="#d9c6b4"/>
        <stop offset="1" stop-color="#c9b78f"/>
      </linearGradient>
    </defs>
    <path d="M0,170 Q220,128 420,188 L0,210 Z" fill="var(--pink-soft)"/>
    <path d="M0,184 Q220,140 440,200 Q470,380 556,492 Q330,610 150,680 Q60,712 0,735 Z" fill="var(--pink)"/>
    <path d="M560,495 Q300,700 0,1060 L0,1095 Q260,760 580,505 Z" fill="var(--pink)"/>
    <path d="M600,515 Q320,700 0,1120 L0,1135 Q330,715 610,520 Z" fill="#dedee2"/>
    <path d="M0,700 Q300,640 620,520" fill="none" stroke="var(--sky)" stroke-width="2"/>
    <path d="M0,745 Q320,650 640,525" fill="none" stroke="var(--sky)" stroke-width="2.5"/>
    <circle cx="706" cy="240" r="272" fill="none" stroke="var(--pink-soft)" stroke-width="10"/>
    <circle cx="706" cy="240" r="262" fill="none" stroke="var(--pink)" stroke-width="9"/>
    <circle cx="706" cy="240" r="256" fill="url(#heroTone)" role="img" aria-label="Photo of a relaxed woman lying back with eyes closed, soft light"/>
    <circle cx="190" cy="731" r="130" fill="var(--pink-soft)"/>
    <circle cx="190" cy="731" r="122" fill="var(--white)"/>
    <circle cx="190" cy="731" r="113" fill="url(#fieldTone)" role="img" aria-label="Photo of women raising joined hands in a sunlit meadow"/>
  </svg>

  <div class="brand"><span class="brand-dot"></span>The Meadow Heart Experience</div>

  <section class="intro">
    <h1 class="title">The Quiet Meadow Renewal Ring</h1>
    <p class="soft" style="top:252px">It’s time to make a commitment….</p>
    <p class="soft" style="top:273px">It’s time for <b>YOU</b>, to <b>SHOW UP for YOU…</b></p>
    <p style="top:311px">It’s time to truly let go…….and finally heal,<br>and find the peace that you so long for…</p>
    <p style="top:360px">You deserve to feel the freedom that comes<br>with truly loving and accepting your body.</p>
    <p style="top:408px">You deserve the freedom that comes with<br>experiencing a deeper trusting connection with<br>your body, where you feel safe, at home.</p>
    <p style="top:476px">Can you even imagine a whole day that you didn’t hate<br>your body, you didn’t fight with food, and you felt<br>peaceful and at home with your body?</p>
    <p class="whisper" style="top:543px">Can you love the part of you, that hates your body?</p>
    <p class="whisper" style="top:571px">You can’t heal something you hate.</p>
  </section>

  <section>
    <div class="pitch call"><p>It’s time to show up for YOU, consistently,</p><p>every week, and do the work,once and for all.</p><p>No more games, no more half in on YOU….</p></div>
    <div class="pitch prison"><p>You deserve better than a life contained in</p><p>the mental prison of body hatred.</p></div>
    <div class="pitch ask"><p>Are you truly ready to make the commitment?</p><p>How would it feel to be able to say,</p><p><em>“I am free to love and accept my body”, and</em></p><p><em>“I am free, connected and at peace to my body”?</em></p></div>
    <div class="pitch invite"><p>I am inviting 10 women only into this six-week healing experience,</p><p>as I personally know, that when we share our stories, it opens our</p><p>hearts for other people to share their stories. It gives us the sense</p><p>we are not alone in our journey’s.</p></div>
    <h2 class="pitch receive">The women that come on this six-week journey will receive;</h2>
    <ul class="benefits">
      <li>Weekly two hour group coaching / sister circle on topics to support a deeper<br>understanding and healing of our relationship with our bodies, and with food</li>
      <li>One 90mins one on one coaching session with me</li>
      <li>Private Meadow Members Group to continue support outside of the circle</li>
      <li>Homework outside of circle to support your healing</li>
      <li>Journal and other small gifts weekly</li>
    </ul>
  </section>

  <section class="details">
    <p class="start">First Round begins Monday 13 November 2017 at Lumen Stones in Glenhaven</p>
    <p class="price">The financial investment in YOU, is $400 for the six weeks. For the women that have attended the Friday night,<br>Gentle Bloom Sister Circle, you will receive a discount of $100, taking the price to $300.</p>
    <p class="early">Early bird discount also available before 31 October.</p>
  </section>

  <footer class="footer">
    <p class="ready">ARE YOU READY?</p>
    <div class="contacts">
      <span><svg viewBox="0 0 20 20"><circle cx="10" cy="10" r="9" fill="none" stroke="#fff" stroke-width="1.6"/><rect x="5" y="6.5" width="10" height="7" fill="#fff"/><path d="M5 6.5 L10 10.5 L15 6.5" fill="none" stroke="#3fc0da" stroke-width="1"/></svg>caroline@carolinebirchwood.com.au</span>
      <span><svg viewBox="0 0 20 20"><circle cx="10" cy="10" r="9" fill="none" stroke="#fff" stroke-width="1.6"/><path d="M6.5 5.5 L8.5 5.5 L9.3 8 L8 9 Q9 11.5 11 12 L12 10.7 L14.5 11.5 L14.5 13.5 Q9 14.5 6.5 5.5 Z" fill="#fff"/></svg>0400 555 127</span>
      <span><svg viewBox="0 0 20 20" fill="none" stroke="#fff" stroke-width="1.3"><circle cx="10" cy="10" r="8.5"/><ellipse cx="10" cy="10" rx="3.5" ry="8.5"/><path d="M1.5 10 H18.5 M3 6 H17 M3 14 H17"/></svg>www.carolinebirchwood.com.au</span>
    </div>
  </footer>
</main>
</body>
</html>
```